Web Design for historic veg friendly, organic restaurant

We need a new web site. The Millbrook Cafe is a 40 year old restaurant in Chicago. We've been one of the premier, casual vegetarian restaurants since we opened. 5 years ago, Millbrook Cafe was purchased from the original owners by a local, certified organic farmer. We are nearly 100% from scratch kitchen, 100% certified organic produce, we are governed by a strict sustainable plan and we are very active politically. But you wouldn't know it form our website! We have a desire to build a simple website around some basic principles:
1. We need our current logo prominently displayed (logo attached)
2. We need a "click to call" easily accessible
3. We have an online order link that needs to be easily accessible
4. We need our hours, location, and directions easy to see
4. We need a separate events page (we have a live music and events venue that runs shows 5-7 nights per week.)
5. We would like to have a separate page for pictures, particularly old pictures. It would be fun to have a function for people to post their own shots, but that might make this too complicated. If it were possible, we would of course need to retain the ability to curate posted pictures.
6. This needs to be easily edited by us, so in a platform such as word press or similar
7. We will need this mobile enhanced

Target Market(s)

Neighborhood residents - zip code is 48213

Industry/Entity Type

Restaurant

Coding

Coded - Design and coding required

Number of Pages Required

4 page

Font styles to use
Sans Serif

Requirements
Must have
• Logo, click to call, events page that we can manage, contact us, about us page, menu (we have the online menu through a third party plugin), a page for our market and some nice pictures on our splash page,
• Must be mobile ready and on a platform such as Word Press or some other platform where we can edit on our own
Nice to have
• Page for past employees and historical pictures, be nice to have food pictures or something similar on a scroll, would love to have an ability for others to post pictures that we would "approve"
Should not have
• We don't need anything that spins, moves, flames or other features that detract from gathering information

```html
<!DOCTYPE html>
<html lang="en">
<head>
<meta charset="utf-8">
<title>Millbrook Cafe</title>
<link rel="stylesheet" href="https://fonts.googleapis.com/css2?family=Lato:wght@400;700;900&family=Roboto:wght@400;500;700&family=Libre+Baskerville:ital@0;1&family=Lobster&family=Open+Sans:wght@400;600&display=swap">
<style>
:root{
  --yellow:#fedd16;
  --black:#000;
  --ink:#1d1d1d;
  --muted:#8a8a8a;
  --cream:#f1f0ec;
  --card:#25272a;
  --line:#dcdcdc;
  --coral:#e06a4f;
}
*{box-sizing:border-box;margin:0;padding:0}
html,body{width:1200px;height:3046px;overflow:hidden;background:#fff}
body{position:relative;font-family:"Open Sans",Arial,sans-serif;color:var(--ink)}

/* header */
.site-header{position:absolute;left:0;top:0;width:1200px;height:66px;background:#fff}
.brand{position:absolute;left:118px;top:0;width:146px;height:80px;background:#fff;box-shadow:0 2px 6px rgba(0,0,0,.15);display:flex;align-items:center;justify-content:center;font:900 19px/1.05 "Lato",sans-serif;color:#b3261e;text-align:center}
.nav{position:absolute;right:110px;top:0;display:flex;height:66px}
.nav a{display:flex;align-items:center;padding:0 14px;font:400 14px "Roboto",sans-serif;color:#222;text-decoration:none}
.nav a.active{background:var(--yellow);padding:0 20px}

/* hero */
.hero{position:absolute;left:0;top:66px;width:1200px;height:575px;background:linear-gradient(120deg,#3b3d3c 0%,#55524a 45%,#8c7a5c 75%,#c9ad80 100%)}
.hero-title{position:absolute;left:0;width:1200px;text-align:center;font-family:"Lobster",cursive;line-height:1}
.hero-title.one{top:180px;font-size:112px;color:#fff}
.hero-title.two{top:300px;font-size:64px;color:var(--yellow);left:40px}

/* reservations */
.reserve{position:absolute;left:425px;top:573px;width:352px;height:253px;background:var(--black);z-index:3;text-align:center}
.reserve-head{height:60px;background:var(--yellow);font:500 25px/60px "Roboto",sans-serif;color:#000}
.reserve p{color:#fff;font:400 15px/1.35 "Roboto",sans-serif;margin:18px 24px 0}
.reserve .phone{font:700 31px "Roboto",sans-serif;color:#fff;margin-top:12px}
.btn-yellow{display:inline-block;margin-top:14px;background:var(--yellow);color:#000;font:500 13px "Roboto",sans-serif;padding:6px 20px;border-radius:6px}

/* intro */
.intro{position:absolute;left:0;top:641px;width:1200px;height:564px;background:var(--cream)}
.intro h2{font:700 50px/1 "Lato",sans-serif;color:#000}
.intro .sub{font:400 20px "Lato",sans-serif;color:#444;margin-top:2px}
.intro p{font:400 12.5px/1.65 "Open Sans",sans-serif;color:var(--muted);margin-top:20px;width:326px}
.intro-left{position:absolute;left:122px;top:236px}
.intro-right{position:absolute;left:750px;top:236px}
.intro-photo{position:absolute;left:530px;top:185px;width:190px;height:360px;background:linear-gradient(180deg,#f2dccb 0%,#d9c2ae 35%,#8fae5a 60%,#3a3a36 100%);border-radius:90px 90px 20px 20px}

/* gallery */
.gallery{position:absolute;left:0;top:1205px;width:1200px;height:501px;background:#fff}
.tile{position:absolute}

/* card shapes */
.card-shape{position:absolute;left:0;top:-20px}

/* events */
.event-card{position:absolute;left:103px;top:1740px;width:420px;height:588px}
.event-inner{position:absolute;left:0;top:0;width:420px;height:588px;text-align:center}
.event-icon{position:absolute;left:180px;top:80px;width:60px;height:60px}
.event-inner h3{position:absolute;top:196px;width:100%;font:400 34px "Libre Baskerville",serif;color:#fff}
.event-inner .tag{position:absolute;top:250px;width:100%;font:italic 400 11px "Libre Baskerville",serif;color:var(--coral);letter-spacing:1.5px}
.event-photo{position:absolute;left:0;top:290px;width:420px;height:298px;background:radial-gradient(ellipse at 60% 45%,#e58d57 0%,#6d4a36 25%,#161616 60%,#000 100%);border-radius:0 0 22px 22px}

.booking{position:absolute;left:580px;top:1780px;width:512px;text-align:center}
.tabs{display:flex;justify-content:center;gap:26px;font:400 18px "Libre Baskerville",serif}
.tabs .on{color:var(--yellow);border-bottom:2px solid var(--yellow);padding-bottom:2px}
.booking .lead{font:400 13px/1.6 "Open Sans",sans-serif;color:#444;margin:34px 10px 0}
.booking h3{font:400 27px "Libre Baskerville",serif;margin-top:22px}
.booking .small{font:400 9px "Open Sans",sans-serif;color:#555;letter-spacing:.5px;margin-top:4px}
.row3{display:flex;justify-content:center;gap:12px;margin-top:22px}
.field-lbl{font:400 9px "Open Sans",sans-serif;color:#555;letter-spacing:.5px;display:block;margin-bottom:8px}
.box{border:1px solid var(--line);height:38px;display:flex;align-items:center;justify-content:center;font:400 12px "Open Sans",sans-serif;color:#333}
.wide{width:512px;justify-content:flex-start;padding-left:12px}
.btn-outline{display:inline-block;margin-top:24px;border:1px solid var(--coral);border-radius:20px;padding:8px 22px;font:400 11px "Open Sans",sans-serif;color:#333}

/* info row */
.hours{position:absolute;left:100px;top:2420px;width:312px}
.hours h3{text-align:center;font:400 22px "Libre Baskerville",serif;margin-bottom:22px}
.hours .r{display:flex;justify-content:space-between;border-bottom:1px solid #ececec;padding:10px 4px;font:400 13px "Open Sans",sans-serif;color:#333}
.directions{position:absolute;left:432px;top:2375px;width:348px;height:266px}
.dir-inner{position:absolute;left:0;top:0;width:348px;height:266px;text-align:center;color:#fff}
.dir-logo{margin-top:20px;font:900 22px "Lato",sans-serif;color:var(--yellow)}
.dir-inner h3{font:400 21px "Libre Baskerville",serif;margin-top:12px}
.dir-inner p{font:600 12.5px/1.6 "Open Sans",sans-serif;margin-top:14px}
.btn-white{display:inline-block;margin-top:18px;background:#fff;color:#222;border-radius:16px;padding:8px 22px;font:400 11px "Open Sans",sans-serif}
.listing{position:absolute;left:800px;width:310px;height:125px;display:flex;align-items:center;justify-content:center}
.listing + .listing{border-top:1px solid #eee}

/* newsletter */
.newsletter{position:absolute;left:0;top:2730px;width:1200px;height:92px;background:var(--yellow)}
.nl-title{position:absolute;left:162px;top:30px;font:400 26px "Lato",sans-serif;color:#000;display:flex;align-items:center;gap:10px}
.nl-input{position:absolute;left:580px;top:23px;width:312px;height:48px;background:#fff;font:italic 13px "Open Sans",sans-serif;color:#999;padding:15px 16px}
.nl-btn{position:absolute;left:892px;top:23px;width:150px;height:48px;background:#000;color:var(--yellow);font:500 16px/48px "Roboto",sans-serif;text-align:center}

/* footer */
.site-footer{position:absolute;left:0;top:2822px;width:1200px;height:224px;background:#000;color:#fff;text-align:center}
.site-footer h4{font:400 18px "Roboto",sans-serif;margin-top:26px}
.social{display:flex;justify-content:center;gap:8px;margin-top:12px}
.social span{width:22px;height:22px;border-radius:50%;background:#fff}
.foot-nav{margin-top:14px;font:400 12px "Roboto",sans-serif;letter-spacing:.5px}
.foot-nav span{margin:0 10px}
.rule{width:780px;height:1px;background:#666;margin:14px auto 0}
.foot-info{font:400 11px/1.8 "Roboto",sans-serif;margin-top:10px}
</style>
</head>
<body>

<header class="site-header">
  <div class="brand">Millbrook<br>Cafe</div>
  <nav class="nav">
    <a class="active">Homes</a><a>About</a><a>Menu</a><a>Reservation</a><a>Gallery</a><a>Contact</a>
  </nav>
</header>

<section class="hero" role="img" aria-label="Overhead photo of sushi table with chopsticks, soy sauce, teapot, rice and ginger root">
  <div class="hero-title one">Welcome To</div>
  <div class="hero-title two">Millbrook Cafe</div>
</section>

<div class="reserve">
  <div class="reserve-head">RESERVATIONS</div>
  <p>Making a reservation at Savoria restaurant is easy and takes just a couple of minutes.</p>
  <div class="phone">+359 555 0142</div>
  <span class="btn-yellow">Book Now</span>
</div>

<section class="intro">
  <div class="intro-left">
    <h2>We offer</h2>
    <div class="sub">Today Specials</div>
    <p>Lorem ipsum dolor sit amet, consectetuer adipiscing elit, sed diam nonummy nibh euismod tincidunt ut laoreet dolore magna aliquam erat volutpat. Ut wisi enim ad minim veniam, quis nostrud exerci tation ullamcorper suscipit lobortis nisl ut aliquip ex ea commodo consequat.</p>
  </div>
  <div class="intro-photo" role="img" aria-label="Hand holding a sushi roll with chopsticks"></div>
  <div class="intro-right">
    <h2>Welcome</h2>
    <div class="sub">Millbrook Cafe</div>
    <p>Lorem ipsum dolor sit amet, consectetuer adipiscing elit, sed diam nonummy nibh euismod tincidunt ut laoreet dolore magna aliquam erat volutpat. Ut wisi enim ad minim veniam, quis nostrud exerci tation ullamcorper suscipit lobortis nisl ut aliquip ex ea commodo consequat.</p>
  </div>
</section>

<section class="gallery">
  <div class="tile" style="left:0;top:0;width:219px;height:222px;background:linear-gradient(135deg,#4a3a2e,#7a5a44 60%,#c8704c)" role="img" aria-label="Sushi platter with teapot"></div>
  <div class="tile" style="left:0;top:226px;width:219px;height:148px;background:linear-gradient(135deg,#2c2622,#7a6a5a 55%,#e0a070)" role="img" aria-label="Sushi rolls close-up"></div>
  <div class="tile" style="left:0;top:378px;width:219px;height:123px;background:linear-gradient(135deg,#2a2522,#6a5446 55%,#d06a4a)" role="img" aria-label="Nigiri on slate with soy sauce"></div>
  <div class="tile" style="left:223px;top:0;width:230px;height:344px;background:linear-gradient(160deg,#c98a7a,#e2b2a2 50%,#a86252)" role="img" aria-label="Cooked octopus tentacles"></div>
  <div class="tile" style="left:223px;top:348px;width:230px;height:153px;background:linear-gradient(135deg,#3a3430,#8e7a66 55%,#d8c2a8)" role="img" aria-label="Chef plating sushi"></div>
  <div class="tile" style="left:457px;top:0;width:743px;height:501px;background:linear-gradient(100deg,#3b2c22,#5a4030 40%,#3a2a20 70%,#4a3626)" role="img" aria-label="Nigiri on black slate with soy sauce dish and chopsticks on wooden table"></div>
</section>

<div class="event-card">
  <svg class="card-shape" width="420" height="628" viewBox="0 -20 420 628" aria-hidden="true"><path d="M0 18 Q0 0 18 0 H180 Q200 0 210 -20 Q220 0 240 0 H402 Q420 0 420 18 V570 Q420 588 402 588 H240 Q220 588 210 606 Q200 588 180 588 H18 Q0 588 0 570 Z" fill="#000"/></svg>
  <div class="event-inner">
    <svg class="event-icon" viewBox="0 0 60 60" aria-hidden="true"><path d="M16 26 Q10 12 24 14 Q30 4 38 14 Q52 12 44 26 Z" fill="none" stroke="#fff" stroke-width="2"/><rect x="18" y="28" width="24" height="8" fill="none" stroke="#fff" stroke-width="2"/><path d="M10 48 H50" stroke="#fff" stroke-width="2"/></svg>
    <h3>PRIVATE EVENTS</h3>
    <div class="tag">~ Find your perfect venue ~</div>
    <div class="event-photo" role="img" aria-label="Sushi on a dark plate with chopsticks and incense smoke"></div>
  </div>
</div>

<section class="booking">
  <div class="tabs"><span class="on">Book a Table</span><span>Events</span></div>
  <p class="lead">Whether you are planning an intimate dinner for friends, a corporate luncheon, or an extravagant soirée, you will find the perfect setting at Savoria.</p>
  <h3>Make a Reservation</h3>
  <div class="small">FOR FURTHER QUESTIONS, PLEASE CALL</div>
  <div class="row3">
    <div><span class="field-lbl">DATE</span><div class="box" style="width:112px">Select Date</div></div>
    <div><span class="field-lbl">TIME</span><div class="box" style="width:84px">1:00am</div></div>
    <div><span class="field-lbl">PARTY SIZE</span><div class="box" style="width:56px">1</div></div>
  </div>
  <span class="field-lbl" style="margin-top:20px">YOUR NAME</span>
  <div class="box wide">Your Name</div>
  <span class="field-lbl" style="margin-top:10px">EMAIL ADDRESS</span>
  <div class="box wide">Email Address</div>
  <span class="btn-outline">Reserve Now</span>
</section>

<section class="hours">
  <h3>Opening Times</h3>
  <div class="r"><span>Week days</span><span>9.00 – 18.00</span></div>
  <div class="r"><span>Saturday</span><span>10.00 – 17.00</span></div>
  <div class="r"><span>Sunday</span><span>Closed</span></div>
</section>

<div class="directions">
  <svg class="card-shape" width="348" height="306" viewBox="0 -20 348 306" aria-hidden="true"><path d="M0 16 Q0 0 16 0 H144 Q164 0 174 -20 Q184 0 204 0 H332 Q348 0 348 16 V250 Q348 266 332 266 H204 Q184 266 174 286 Q164 266 144 266 H16 Q0 266 0 250 Z" fill="#25272a"/></svg>
  <div class="dir-inner">
    <div class="dir-logo">Millbrook Cafe</div>
    <h3>Directions</h3>
    <p>Millbrook, IL<br>24 Hollow Lane, Eastfield</p>
    <span class="btn-white">View on map</span>
  </div>
</div>

<div class="listing" style="top:2380px"><svg width="60" height="40" aria-hidden="true"><rect x="10" y="4" width="40" height="32" rx="6" fill="#e2335a"/></svg></div>
<div class="listing" style="top:2505px"><svg width="60" height="40" aria-hidden="true"><rect x="10" y="4" width="40" height="32" rx="6" fill="#d32323"/></svg></div>

<section class="newsletter">
  <div class="nl-title">
    <svg width="44" height="30" viewBox="0 0 44 30" aria-hidden="true"><rect x="1" y="1" width="42" height="28" fill="#000"/><path d="M1 1 L22 17 L43 1" fill="none" stroke="#fedd16" stroke-width="2"/></svg>
    Subscribe to our Newsletter
  </div>
  <div class="nl-input">Your Email Address...</div>
  <div class="nl-btn">SUBSCRIBE</div>
</section>

<footer class="site-footer">
  <h4>CONNECT WITH US</h4>
  <div class="social"><span></span><span></span><span></span><span></span></div>
  <div class="foot-nav"><span>HOME</span>|<span>GALLERY</span>|<span>SPECIALTY SERVICES</span>|<span>ABOUT</span>|<span>CONTACT</span></div>
  <div class="rule"></div>
  <svg width="14" height="20" viewBox="0 0 14 20" style="margin-top:12px" aria-hidden="true"><path d="M7 0 A7 7 0 0 1 14 7 C14 12 7 20 7 20 C7 20 0 12 0 7 A7 7 0 0 1 7 0 Z" fill="#fff"/><circle cx="7" cy="7" r="2.5" fill="#000"/></svg>
  <div class="foot-info">Millbrook Cafe, 24 Hollow Lane, Suite B Eastfield, IL 48213 (555) 010-2266<br>© Copyright 2017 Millbrook Cafe . Disclaimer | &nbsp;Privacy &nbsp;| &nbsp;Site Map</div>
</footer>

</body>
</html>
```